Sun-Pod Coffee Kiosks Webdesign project

Sun-Pod Coffee Kiosks provides coffee carts, kiosks, and/or drive thrus depending on location. At Sun-Pod our company focuses on offering healthy snack & drink options for people on the go as well as nutritional coaching with our daily "Pod notes." We will provide some healthy snacks as well.

We offer all organic coffee & espresso drinks,100% real fruit & vegetable smoothies, protein shakes, and healthy breakfast/snack items.

I want "balance" to be a big theme in the website design. True well-being is a balance of body (health), mind (emotional well-being) and spirit (we are a Christian based company who loves and accepts all people, sexual orientation, religions, ect)

My parents are missionaries and founded the Nicaraguan organization "Bright Path Outreach Nicaragua" over 11 years ago ( www.brightpathoutreach.org ). Sun-Pod plans to be a financial partner to their mission so 10% of profits or 2% of total revenue, whichever is greater will go to Bright Path and their church plants & medical/dental clinic. I want this and info about Bright Path to have a page on the website.

Target Market(s)

Ages 18-54 (target coffee customer).

Industry/Entity Type

Financial

Requirements
Must have
• -Home page
-Menu page
-Locations page/contact page
-Kiosk options page (cart, kiosk & drive thru descriptions, pics, traffic & location needs, ect)
-Fundraising/Bright Path Outreach Nicaragua page
Nice to have
• I have a logo designed that I attached. I would like the colors to be dark brown, light brown, and a lime green. My business card is also attached.

```html
<!DOCTYPE html>
<html lang="en">
<head>
<meta charset="utf-8">
<title>Sun-Pod Organic Coffee</title>
<link rel="stylesheet" href="https://fonts.googleapis.com/css2?family=Roboto+Condensed:wght@300;400;700&family=Yanone+Kaffeesatz:wght@500&display=swap">
<style>
  :root {
    --lime: #abd04b;
    --lime-dark: #6faa1e;
    --brown-dark: #3f2414;
    --brown-mid: #6b3a22;
    --brown-footer: #813e28;
    --rust-text: #c8613a;
    --bullet-green: #27e02c;
    --dot-grey: #a9a9a9;
    --white: #ffffff;
  }
  html, body {
    margin: 0;
    padding: 0;
    width: 1200px;
    height: 1200px;
    overflow: hidden;
  }
  body {
    position: relative;
    font-family: "Roboto Condensed", "Arial Narrow", sans-serif;
    background: var(--white);
  }
  .site-header {
    position: absolute;
    left: 0; top: 0;
    width: 1200px; height: 290px;
    background: var(--lime);
  }
  .brand {
    position: absolute;
    left: 64px; top: 128px;
    width: 330px;
    text-align: center;
  }
  .brand-name {
    display: block;
    font-family: "Yanone Kaffeesatz", "Roboto Condensed", sans-serif;
    font-weight: 500;
    font-size: 100px;
    line-height: 1;
    color: var(--brown-dark);
  }
  .brand-tagline {
    display: block;
    margin-top: 4px;
    font-weight: 700;
    font-size: 18px;
    letter-spacing: 3.5px;
    color: var(--brown-mid);
  }
  .search {
    position: absolute;
    left: 658px; top: 38px;
    display: flex;
    align-items: center;
    gap: 11px;
  }
  .search-button {
    width: 112px; height: 38px;
    border-radius: 6px;
    background: linear-gradient(#8a4a2c, #5e2f1a);
    color: var(--white);
    font-family: Arial, sans-serif;
    font-weight: 700;
    font-size: 24px;
    line-height: 38px;
    text-align: center;
  }
  .search-field {
    width: 370px; height: 42px;
    background: var(--white);
    border: 3px solid #9a9a9a;
  }
  .main-nav {
    position: absolute;
    left: 558px; top: 238px;
    height: 52px;
    display: flex;
  }
  .main-nav a {
    display: block;
    height: 52px;
    line-height: 54px;
    font-weight: 300;
    font-size: 33px;
    color: var(--brown-mid);
    text-decoration: none;
    white-space: nowrap;
  }
  .main-nav .is-current {
    width: 93px;
    text-align: center;
    background: var(--lime-dark);
  }
  .nav-about { margin-left: 31px; }
  .nav-gallery { margin-left: 44px; }
  .nav-contact { margin-left: 29px; }

  .hero {
    position: absolute;
    left: 0; top: 290px;
    width: 1200px; height: 716px;
    background:
      radial-gradient(ellipse 180px 260px at 1000px 560px, #6c8a3c 0%, rgba(108,138,60,0) 100%),
      radial-gradient(ellipse 160px 120px at 880px 120px, #e9e6e1 0%, rgba(233,230,225,0) 100%),
      linear-gradient(100deg, #c9ad86 0%, #a7825d 30%, #6a3c21 55%, #4d2715 80%, #3e1f10 100%);
  }
  .hero-panel {
    position: absolute;
    left: 0; top: 50px;
    width: 1034px; height: 504px;
    background: rgba(92, 52, 36, 0.62);
  }
  .hero-list {
    list-style: none;
    margin: 0;
    padding: 0;
    position: absolute;
    left: 54px; top: 46px;
  }
  .hero-list li {
    position: relative;
    padding-left: 32px;
    height: 60px;
    font-weight: 400;
    font-size: 43px;
    line-height: 60px;
    color: var(--white);
    white-space: nowrap;
    letter-spacing: -0.3px;
  }
  .hero-list li::before {
    content: "";
    position: absolute;
    left: 0; top: 18px;
    width: 24px; height: 24px;
    border-radius: 50%;
    background: var(--bullet-green);
  }
  .slider-dots {
    position: absolute;
    left: 1008px; top: 672px;
    display: flex;
    gap: 21px;
  }
  .slider-dots span {
    width: 28px; height: 28px;
    border-radius: 50%;
    background: var(--dot-grey);
  }
  .slider-dots .is-active { background: var(--bullet-green); }

  .contact-block {
    position: absolute;
    left: 0; top: 1006px;
    width: 674px; height: 194px;
    background: var(--brown-footer);
  }
  .contact-block address {
    position: absolute;
    left: 35px; top: 37px;
    font-style: normal;
    font-size: 20px;
    line-height: 29.7px;
    color: var(--white);
  }
  .mission-block {
    position: absolute;
    left: 674px; top: 1006px;
    width: 526px; height: 194px;
  }
  .mission-text {
    position: absolute;
    left: 0; top: 46px;
    width: 262px;
    text-align: center;
    font-size: 19.5px;
    line-height: 29px;
    color: var(--rust-text);
  }
  .mission-link {
    display: block;
    margin-top: 10px;
    font-family: Arial, sans-serif;
    font-size: 18px;
  }
  .partner-name {
    position: absolute;
    left: 262px; top: 70px;
    width: 260px;
    display: flex;
    align-items: center;
    gap: 10px;
    font-weight: 700;
    font-size: 38px;
    color: #1f2a8c;
    white-space: nowrap;
  }
  .partner-mark {
    width: 22px; height: 22px;
    border-radius: 50%;
    background: #f0a42a;
  }
</style>
</head>
<body>
  <header class="site-header">
    <div class="brand">
      <span class="brand-name">Sun-Pod</span>
      <span class="brand-tagline">ORGANIC COFFEE</span>
    </div>
    <div class="search">
      <div class="search-button">SEARCH</div>
      <div class="search-field"></div>
    </div>
    <nav class="main-nav">
      <a class="is-current" href="#">HOME</a>
      <a class="nav-about" href="#">ABOUT US</a>
      <a class="nav-gallery" href="#">GALLERY</a>
      <a class="nav-contact" href="#">CONTACT US</a>
    </nav>
  </header>

  <section class="hero" role="img" aria-label="Roasted coffee beans spilling from a white cup onto burlap, with a green coffee leaf">
    <div class="hero-panel">
      <ul class="hero-list">
        <li>Organic coffee, espresso &amp; tea</li>
        <li>BlendPro smoothies &amp; protein shakes</li>
        <li>Healthy bites, on the go!</li>
        <li>Call about Catering / Coffee Delivery</li>
      </ul>
    </div>
    <div class="slider-dots">
      <span class="is-active"></span><span></span><span></span><span></span>
    </div>
  </section>

  <footer>
    <div class="contact-block">
      <address>
        2140 Maple Glen Ct.<br>
        Cedarville, NC, 27000<br>
        555-013-4872<br>
        hello@sun-pod.com
      </address>
    </div>
    <div class="mission-block">
      <p class="mission-text" style="margin:0">
        10% of all profits help fund<br>
        Bright Path Outreach Nicaragua
        <span class="mission-link">www.brightpathoutreach.org</span>
      </p>
      <div class="partner-name"><span class="partner-mark"></span>Bright Path</div>
    </div>
  </footer>
</body>
</html>
```